Marketing company needs business card design

Our company (Ventures Beyond Harbor) need a business card design for a marketing company. The design should of course include the logo and business colors (orange and blue). I would like the design to be clean and professional. The business card is going to be a die cut card that is leaf shaped (I have uploaded the template for it). I would love to see a design that is professional but nothing too "corporate."
Updates

Hello everyone,

Just wanted to let you know that I have uploaded an AI and EPS version of the logo for your convenience.

Thank you!

~Marlene

Industry/Entity Type

Marketing

Requirements
Must have
• Must have the following contact info:

Ventures Beyond Harbor
2817 Hollow Brook Ln B204
Prescott, AZ 86517

928.471.6083

info@venturesbeyondharbor-example.com

```html
<!DOCTYPE html>
<html lang="en">
<head>
<meta charset="utf-8">
<title>Ventures Beyond Harbor – Business Card</title>
<link rel="stylesheet" href="https://fonts.googleapis.com/css2?family=Marcellus&family=PT+Sans:wght@400;700&display=swap">
<style>
  :root {
    --brand-blue: #12ade6;
    --brand-orange: #efac63;
    --paper: #ffffff;
    --backdrop: #eeeeee;
    --leaf-radius: 180px;
  }
  * { margin: 0; padding: 0; box-sizing: border-box; }
  html, body {
    width: 1152px;
    height: 1200px;
    overflow: hidden;
    background: var(--backdrop);
  }
  .card {
    position: absolute;
    left: 144px;
    width: 864px;
    height: 492px;
    overflow: hidden;
  }
  .card--front {
    top: 86px;
    background: var(--brand-blue);
    border-radius: var(--leaf-radius) 0 var(--leaf-radius) 0;
  }
  .card--back {
    top: 622px;
    background: var(--paper);
    border-radius: 0 var(--leaf-radius) 0 var(--leaf-radius);
  }

  .brand-name {
    font-family: "Marcellus", serif;
    font-weight: 400;
    line-height: 1.05;
  }
  .card--front .brand {
    position: absolute;
    left: 190px;
    top: 190px;
    display: flex;
    align-items: center;
    gap: 28px;
  }
  .brand-dot {
    width: 64px;
    height: 64px;
    border-radius: 50%;
    background: var(--brand-orange);
    flex: none;
  }
  .card--front .brand-name { color: var(--paper); font-size: 60px; }

  .card--back .brand-name {
    position: absolute;
    right: 58px;
    top: 66px;
    text-align: right;
    color: var(--brand-blue);
    font-size: 46px;
  }
  .wave { position: absolute; left: 0; top: 0; width: 864px; height: 492px; }
  .wave path { fill: var(--brand-blue); }

  .contact {
    position: absolute;
    right: 48px;
    top: 282px;
    width: 540px;
    text-align: right;
    color: var(--paper);
    font-family: "PT Sans", sans-serif;
    font-style: normal;
    font-size: 22px;
    line-height: 30px;
    white-space: nowrap;
  }
  .contact__company { font-weight: 700; }
  .contact__rule {
    height: 2px;
    background: var(--paper);
    opacity: .85;
    margin: 10px 0 12px 140px;
  }
  .contact__line { display: flex; justify-content: flex-end; align-items: center; gap: 10px; }
  .contact__icon { width: 18px; height: 18px; fill: var(--paper); flex: none; }
</style>
</head>
<body>
  <section class="card card--front" aria-label="Card front">
    <div class="brand">
      <span class="brand-dot"></span>
      <div class="brand-name">Ventures Beyond<br>Harbor</div>
    </div>
  </section>

  <section class="card card--back" aria-label="Card back">
    <svg class="wave" viewBox="0 0 864 492" aria-hidden="true">
      <path d="M0 320 C 280 270, 580 260, 864 190 L864 492 L0 492 Z"/>
    </svg>
    <div class="brand-name">Ventures Beyond<br>Harbor</div>
    <address class="contact">
      <div class="contact__company">Ventures Beyond Harbor</div>
      <div>2817 Hollow Brook Ln B204</div>
      <div>Prescott, AZ 86517</div>
      <div class="contact__rule"></div>
      <div class="contact__line">928.471.6083
        <svg class="contact__icon" viewBox="0 0 18 18" aria-label="phone"><path d="M5 1h8a1 1 0 0 1 1 1v14a1 1 0 0 1-1 1H5a1 1 0 0 1-1-1V2a1 1 0 0 1 1-1zm1 2v9h6V3zm3 10.5a1 1 0 1 0 0 2 1 1 0 0 0 0-2z"/></svg>
      </div>
      <div class="contact__line">info@venturesbeyondharbor-example.com
        <svg class="contact__icon" viewBox="0 0 18 18" aria-label="email"><path d="M1 4h16v10H1zm1.5 1.2L9 10l6.5-4.8V5h-13z"/></svg>
      </div>
    </address>
  </section>
</body>
</html>
```